Professional Business Card for Commercial Cleaning Company

We need a business card that represents our commercial janitorial cleaning company and represent several brands for our company so we do not want to highlight the logo too much. We want something that says we are professional.
Notes:No website or address as we have many locations and many websites and companies under our corporate name of "Brightwell Holdings, LLC" . Every time we hand a customer a business card they have contacted us via another brand we own but we don't want to have 21 business cards so we want to not focus on Brightwell Holdings, LLC too much since people will automatically ask "What is Brightwell Holdings, LLC" Example: Noodle Barn and Wrap Dome restaurants are owned by "Zing! Brands" is the corporation name. Same principle here. Except we do not advertise at this time that all of our brands are connected. Hope this helps.
Target Market(s)
Commercial Cleaning
Industry/Entity Type
Janitorial Service
Contact Information for Business Card
Miles Hartwin
Business Development
347-628-9043
sales@brightwellholdingsllc.example
Requirements
Must have
- Logo with contact information, need to be able to easily edit contact info for others in my office.
Nice to have
- Professional Image. Like to see a colorful bold look and a more standard business card look.
Should not have
- Any type of cleaning icons, tools, people or water.

```html
<!DOCTYPE html>
<html lang="en">
<head>
<meta charset="utf-8">
<title>Brightwell Holdings, LLC — Business Card</title>
<link rel="stylesheet" href="https://fonts.googleapis.com/css2?family=Poppins:wght@600&family=Lato:wght@400&display=swap">
<style>
  :root {
    --navy: #2d3e72;
    --green: #72a043;
    --ink: #3a3f4a;
    --paper: #ffffff;
    --backdrop: #e7e3da;
    --shadow: rgba(60, 50, 35, 0.22);
  }
  * { margin: 0; padding: 0; box-sizing: border-box; }
  html, body {
    width: 1200px;
    height: 1200px;
    overflow: hidden;
    background: var(--backdrop);
  }
  .canvas {
    position: relative;
    width: 1200px;
    height: 1200px;
  }
  .card {
    position: absolute;
    left: 229px;
    width: 744px;
    height: 424px;
    background: var(--paper);
    box-shadow: 0 18px 24px -14px var(--shadow);
  }
  .card--front { top: 147px; }
  .card--back { top: 640px; }

  .brand-name {
    position: absolute;
    left: 0;
    right: 0;
    top: 170px;
    text-align: center;
    font-family: "Poppins", sans-serif;
    font-weight: 600;
    font-size: 54px;
    letter-spacing: -1px;
    line-height: 1;
    color: var(--navy);
  }

  .person {
    position: absolute;
    right: 433px;
    top: 208px;
    text-align: right;
  }
  .person__name {
    font-family: "Poppins", sans-serif;
    font-weight: 600;
    font-size: 31px;
    letter-spacing: -0.5px;
    line-height: 1;
    color: var(--navy);
    text-transform: uppercase;
  }
  .person__role {
    margin-top: 3px;
    font-family: "Lato", sans-serif;
    font-size: 18px;
    letter-spacing: 0.6px;
    color: var(--ink);
  }

  .contact {
    position: absolute;
    left: 350px;
    top: 219px;
    list-style: none;
    font-family: "Lato", sans-serif;
    font-size: 17.5px;
    letter-spacing: 0.6px;
    color: var(--ink);
  }
  .contact__item {
    display: flex;
    align-items: center;
    gap: 10px;
    height: 26px;
  }
  .contact__icon {
    width: 17px;
    height: 17px;
    flex: none;
    fill: var(--green);
  }
</style>
</head>
<body>
<main class="canvas">
  <section class="card card--front" aria-label="Card front">
    <h1 class="brand-name">Brightwell Holdings, LLC</h1>
  </section>

  <section class="card card--back" aria-label="Card back">
    <div class="person">
      <p class="person__name">Miles Hartwin</p>
      <p class="person__role">Business Development</p>
    </div>
    <ul class="contact">
      <li class="contact__item">
        <svg class="contact__icon" viewBox="0 0 24 24" aria-hidden="true">
          <path d="M6.6 10.8c1.4 2.8 3.8 5.1 6.6 6.6l2.2-2.2c.3-.3.7-.4 1-.2 1.1.4 2.3.6 3.6.6.6 0 1 .4 1 1V20c0 .6-.4 1-1 1C10.6 21 3 13.4 3 4c0-.6.4-1 1-1h3.5c.6 0 1 .4 1 1 0 1.3.2 2.5.6 3.6.1.3 0 .7-.2 1z"/>
        </svg>
        <span>347-628-9043</span>
      </li>
      <li class="contact__item">
        <svg class="contact__icon" viewBox="0 0 24 24" aria-hidden="true">
          <path d="M2 6.5V19h20V6.5l-10 6.5z"/>
          <path d="M2 5h20l-10 6.5z"/>
        </svg>
        <span>sales@brightwellholdingsllc.example</span>
      </li>
    </ul>
  </section>
</main>
</body>
</html>
```